Business Card Design

We are an IT staffing and consulting company providing IT solutions and resources to our clients.

Industry/Entity Type

Business

Contact Information for Business Card

Ramesh Tulavarthi
Vice President

BrightNode Inc
48215 Harrowmere Court Square, suite 700
Ashburn, VA 20147
Direct: 571-555-0193
Mobile: 571-555-0147
Email: Ramesh@brightnodeinc.com
Fax: 703-555-0162
www.brightnodeinc.com

```html
<!DOCTYPE html>
<html lang="en">
<head>
<meta charset="utf-8">
<title>BrightNode Inc – Business Card</title>
<link rel="stylesheet" href="https://fonts.googleapis.com/css2?family=Michroma&display=swap">
<style>
  :root {
    --backdrop: #e4e4e4;
    --card-white: #ffffff;
    --card-grey: #e9e9ea;
    --ink: #1b1b1b;
    --ink-soft: #4a4a4a;
    --band-black: #050505;
    --accent-red: #c8202f;
    --on-black: #f2f2f2;
  }
  * { margin: 0; padding: 0; box-sizing: border-box; }
  html, body { width: 1200px; height: 900px; overflow: hidden; }
  body {
    background: var(--backdrop);
    font-family: "Michroma", sans-serif;
    color: var(--ink);
    display: flex;
    flex-direction: column;
    align-items: center;
    justify-content: center;
    gap: 36px;
  }
  .card {
    position: relative;
    width: 720px;
    height: 411px;
    border-radius: 40px;
    overflow: hidden;
    background: radial-gradient(ellipse at 60% 40%, var(--card-white) 0%, var(--card-grey) 100%);
    box-shadow: 0 10px 24px rgba(0,0,0,0.18);
  }
  .card-art { position: absolute; inset: 0; }
  .brand {
    position: absolute;
    display: flex;
    align-items: center;
    gap: 10px;
    color: var(--ink);
    letter-spacing: 1px;
  }
  .brand-dot {
    border-radius: 50%;
    background: var(--accent-red);
    flex: none;
  }
  .front .brand { left: 44px; top: 40px; font-size: 30px; }
  .front .brand-dot { width: 16px; height: 16px; }
  .holder { position: absolute; left: 44px; top: 104px; }
  .holder-name {
    font-size: 15px;
    font-variant: small-caps;
    letter-spacing: 2px;
    color: var(--ink);
  }
  .holder-title {
    margin-top: 6px;
    font-size: 13px;
    font-variant: small-caps;
    letter-spacing: 2px;
    color: var(--ink-soft);
  }
  .contact {
    position: absolute;
    left: 380px;
    top: 266px;
    list-style: none;
    color: var(--on-black);
    font-size: 10px;
    line-height: 17px;
    letter-spacing: 0.6px;
  }
  .contact li { display: flex; align-items: flex-start; gap: 8px; }
  .contact .icon {
    flex: none;
    width: 13px; height: 13px;
    margin-top: 2px;
  }
  .contact .no-icon { padding-left: 21px; }
  .back .brand {
    left: 50%; top: 50%;
    transform: translate(-50%, -50%);
    font-size: 44px;
  }
  .back .brand-dot { width: 22px; height: 22px; }
</style>
</head>
<body>

<section class="card front" aria-label="Business card front">
  <svg class="card-art" viewBox="0 0 720 411" aria-hidden="true">
    <path d="M0,186 C220,296 500,276 720,136 L720,411 L0,411 Z" fill="var(--band-black)"/>
    <path d="M0,170 C220,280 500,260 720,120" fill="none" stroke="var(--accent-red)" stroke-width="5"/>
  </svg>

  <div class="brand"><span class="brand-dot"></span>BrightNode</div>

  <div class="holder">
    <p class="holder-name">Ramesh Tulavarthi</p>
    <p class="holder-title">Vice President</p>
  </div>

  <ul class="contact">
    <li>
      <svg class="icon" viewBox="0 0 14 14"><circle cx="7" cy="7" r="7" fill="#fff"/><path d="M7 3a2.4 2.4 0 0 0-2.4 2.4C4.6 7.4 7 10.5 7 10.5s2.4-3.1 2.4-5.1A2.4 2.4 0 0 0 7 3z" fill="#000"/></svg>
      <span>48215 Harrowmere Court Square,</span>
    </li>
    <li class="no-icon">suite 700, Ashburn, VA 20147</li>
    <li>
      <svg class="icon" viewBox="0 0 14 14"><circle cx="7" cy="7" r="7" fill="#fff"/><path d="M4.5 3.5l1.5 0 .7 2-1 .8a5 5 0 0 0 2 2l.8-1 2 .7v1.5c0 .5-.5 1-1 1A6 6 0 0 1 3.5 4.5c0-.5.5-1 1-1z" fill="#000"/></svg>
      <span>571-555-0193</span>
    </li>
    <li>
      <svg class="icon" viewBox="0 0 14 14"><circle cx="7" cy="7" r="7" fill="#fff"/><rect x="5" y="3" width="4" height="8" rx="0.8" fill="#000"/></svg>
      <span>571-555-0147</span>
    </li>
    <li>
      <svg class="icon" viewBox="0 0 14 14"><circle cx="7" cy="7" r="7" fill="#fff"/><rect x="3.5" y="5.5" width="7" height="4.5" fill="#000"/><rect x="5" y="3.5" width="4" height="2" fill="#000"/></svg>
      <span>703-555-0162</span>
    </li>
    <li>
      <svg class="icon" viewBox="0 0 14 14"><circle cx="7" cy="7" r="7" fill="#fff"/><rect x="3.5" y="4.5" width="7" height="5" fill="#000"/><path d="M3.5 4.5L7 7.5l3.5-3" fill="none" stroke="#fff" stroke-width="0.8"/></svg>
      <span>Ramesh@brightnodeinc.com</span>
    </li>
    <li>
      <svg class="icon" viewBox="0 0 14 14"><circle cx="7" cy="7" r="7" fill="#fff"/><circle cx="7" cy="7" r="3.6" fill="none" stroke="#000" stroke-width="0.9"/><path d="M3.4 7h7.2M7 3.4c-1.6 2-1.6 5.2 0 7.2M7 3.4c1.6 2 1.6 5.2 0 7.2" fill="none" stroke="#000" stroke-width="0.8"/></svg>
      <span>www.brightnodeinc.com</span>
    </li>
  </ul>
</section>

<section class="card back" aria-label="Business card back">
  <div class="brand"><span class="brand-dot"></span>BrightNode</div>
</section>

</body>
</html>
```